Business Cards Needed for Innovative Healthcare Marketing Company

We are a marketing company focused on healthcare. Our company is all about rebranding yourself renewing your image and generating results. The phoenix stands for "reborn" or "rising" which we provide new brands for our clients we take their old brands and renew it with creativity and innovation. I am looking for a business card with color dimension. I have attached an example of a card I think has the look and feel of what I am trying to accomplish. I like that the card example has black and grey font colors, I like the font placement and the small logo, I really like the use of the colors on the right those are the colors of my logo. My logo is phoenix so maybe incorporating flames similar to that design. I would like the back a solid color maybe red with an opaque version of the logo and website. As a marketing company I am always open to creative liberty!

Target Market(s)

Doctors and business professionals.

Industry/Entity Type

Marketing

Contact Information for Business Card

Vornaly Health Care Marketing
Marnie Okonski- CEO
#(502)638-2947
email-marnie@vornaly.com
website- vornaly.com

Font styles to use
Sans Serif

Colors
ec1f27
f37122
ffc214
fbed22
fbf289
f04a50

Requirements
Must have
• The logo and required information
Nice to have
• icons by the information
Should not have
• child like font

```html
<!DOCTYPE html>
<html lang="en">
<head>
<meta charset="utf-8">
<title>Vornaly Health Care Marketing – Business Card</title>
<link href="https://fonts.googleapis.com/css2?family=Open+Sans:wght@400;600;700&display=swap" rel="stylesheet">
<style>
  :root{
    --stage:#3b3b3b;
    --paper:#ffffff;
    --ink:#0b0b0b;
    --red:#ec1f27;
    --frame-red:#b3202a;
    --orange:#f37122;
    --amber:#ffc214;
    --white:#ffffff;
  }
  *{margin:0;padding:0;box-sizing:border-box}
  html,body{width:1200px;height:950px;overflow:hidden}
  body{background:var(--stage);font-family:"Open Sans",Arial,sans-serif;position:relative}

  .card{position:absolute;left:310px;width:580px;height:350px;border-radius:24px;overflow:hidden}
  .card__frame{position:absolute;inset:14px;border:2px solid var(--frame-red);border-radius:16px}

  .card--front{top:80px;background:var(--paper)}
  .front-brand{position:absolute;inset:0;display:flex;align-items:center;justify-content:center;gap:18px}
  .brand-dot{width:54px;height:54px;border-radius:50%;background:var(--orange)}
  .brand-name{color:var(--red);font-weight:400;font-size:40px;letter-spacing:2px;line-height:1}
  .brand-name small{display:block;font-size:12px;letter-spacing:1.5px;margin-top:6px}

  .card--back{top:500px;background:var(--ink)}
  .back-mark{position:absolute;right:48px;top:48px;display:flex;align-items:center;gap:12px}
  .back-mark .brand-dot{width:90px;height:90px;background:linear-gradient(160deg,var(--red),var(--orange) 60%,var(--amber))}
  .back-mark .mark-name{color:var(--orange);font-size:18px;font-weight:600;letter-spacing:2px}

  .contact{position:absolute;left:60px;top:80px;list-style:none;color:var(--white)}
  .contact li{display:flex;align-items:center;gap:14px;margin-bottom:18px;font-size:16px}
  .contact .icon{width:24px;height:24px;border-radius:4px;background:var(--red);display:flex;align-items:center;justify-content:center;flex:none}
  .contact .person-name{color:var(--red);font-weight:700;font-size:21px;line-height:1.1}
  .contact .person-role{color:var(--white);font-weight:700;font-size:15px;margin-top:2px}
</style>
</head>
<body>

<section class="card card--front">
  <div class="card__frame"></div>
  <div class="front-brand">
    <div class="brand-dot"></div>
    <div class="brand-name">VORNALY<small>HEALTHCARE MARKETING</small></div>
  </div>
</section>

<section class="card card--back">
  <div class="card__frame"></div>

  <div class="back-mark">
    <span class="mark-name">VORNALY</span>
    <div class="brand-dot"></div>
  </div>

  <ul class="contact">
    <li>
      <span class="icon"><svg width="14" height="14" viewBox="0 0 14 14"><circle cx="7" cy="4.5" r="3" fill="#fff"/><path d="M1.5 13.5c0-3.2 2.5-5 5.5-5s5.5 1.8 5.5 5z" fill="#fff"/></svg></span>
      <div><div class="person-name">Marnie Okonski</div><div class="person-role">CEO</div></div>
    </li>
    <li>
      <span class="icon"><svg width="14" height="14" viewBox="0 0 14 14"><path d="M3 1.5l2.2 0 1 3-1.5 1.1c.7 1.5 1.8 2.6 3.3 3.3l1.1-1.5 3 1v2.2c0 .8-.7 1.4-1.5 1.4C5.7 12 2 8.3 1.6 3 1.6 2.2 2.2 1.5 3 1.5z" fill="#fff"/></svg></span>
      <span>(502)638-2947</span>
    </li>
    <li>
      <span class="icon"><svg width="14" height="14" viewBox="0 0 14 14"><rect x="1" y="3" width="12" height="8" rx="1" fill="#fff"/><path d="M1.5 3.5L7 8l5.5-4.5" fill="none" stroke="#ec1f27" stroke-width="1.2"/></svg></span>
      <span>marnie@vornaly.com</span>
    </li>
    <li>
      <span class="icon"><svg width="14" height="14" viewBox="0 0 14 14"><circle cx="7" cy="7" r="5.5" fill="none" stroke="#fff" stroke-width="1.4"/><ellipse cx="7" cy="7" rx="2.3" ry="5.5" fill="none" stroke="#fff" stroke-width="1.1"/><path d="M1.5 7h11" stroke="#fff" stroke-width="1.1"/></svg></span>
      <span>www.vornaly.com</span>
    </li>
  </ul>
</section>

</body>
</html>
```